Cookie needs a website

We need a website for a cookie company based in Mexico City. Our company (called Panes Doradillos) has been baking and crating all sorts of cookies and cakes for more than 35 years.
We started off as a family business and till this date we are still functioning as one. We need the design of the web to be more on the baking side as we have many types of cookies cakes, pastries & muffins. Key elements, home style baking, use colours black, white and red. Tabs we need: front page, who are we, our brands and contact Preferable in Spanish. Im sure you have questions, please contact us. This is for homepage PSD design only no CSS,XHTML or full website build or coding involved as this is design competition.
Updates

Some more information has been added. Thanks is advance for your talent!

Target Market(s)

Target is general public, mostly families. Our product is not a luxury good,more like an affordable treat, however we do use very high quality products and high quality standards. Our motive is natural ingredients and home baked goods.
Our main point of sales is having shops inside department stores. Our own shops and selling to other businesses for re sale

Industry/Entity Type

Business

Font styles to use
Serif

Colors
ec2027
ffffff
333333

Requirements
Must have
• Baking oriented. An oven would be nice since we bake in front of our clients.
Colors we use also important
Nice to have
• make it home. (you have design freedom)
Below are the logos PD is the company name. Tomelo is one of our branches and the the pictures are from the cookies we make
Should not have
• PLEASE NO corny, over colorfull or tacky designs!!

```html
<!DOCTYPE html>
<html lang="es">
<head>
<meta charset="utf-8">
<title>Panes Doradillos — Inicio</title>
<link href="https://fonts.googleapis.com/css2?family=Aleo:wght@300;400;700&family=Open+Sans:ital,wght@0,400;0,600;0,700;1,400&display=swap" rel="stylesheet">
<style>
:root{
  --red:#ec2027;
  --red-deep:#c9161d;
  --ink:#333333;
  --muted:#8a8a8a;
  --white:#ffffff;
  --black:#121212;
  --line:#e2e2e2;
  --tab:#e4e4e4;
}
*{box-sizing:border-box;margin:0;padding:0}
html,body{width:1200px;height:2632px;overflow:hidden;background:var(--white)}
body{position:relative;font-family:"Open Sans",Arial,sans-serif;color:var(--ink)}
.abs{position:absolute}
.serif{font-family:"Aleo",Georgia,serif}

/* hero */
.hero{left:0;top:0;width:1200px;height:591px;overflow:hidden}
.hero-photo{position:absolute;inset:0;background:
  radial-gradient(ellipse 520px 300px at 250px 360px,#6b5237 0%,transparent 70%),
  radial-gradient(ellipse 460px 260px at 1000px 200px,#5a4330 0%,transparent 70%),
  linear-gradient(180deg,#2a1f18 0%,#1d1611 55%,#2b2119 100%)}
.hero-shade{position:absolute;inset:0;background:rgba(0,0,0,.25)}
.menu-icon{left:98px;top:30px;width:56px;height:26px}
.menu-icon span{display:block;height:3px;background:var(--white);margin-bottom:8px}
.brand-badge{left:510px;top:193px;width:176px;height:176px;border-radius:50%;background:var(--black);border:4px solid var(--white);display:flex;align-items:center;justify-content:center;text-align:center}
.brand-badge span{font-family:"Aleo",Georgia,serif;font-weight:700;color:var(--white);font-size:20px;line-height:1.2;text-transform:uppercase;letter-spacing:1px}
.hero-title{left:0;top:428px;width:1200px;text-align:center;font-family:"Aleo",Georgia,serif;font-weight:300;color:var(--white);font-size:34px;line-height:42px}
.hero-title strong{font-weight:700}
.dots{left:580px;top:540px;display:flex;gap:10px}
.dots i{width:10px;height:10px;border-radius:50%;background:rgba(255,255,255,.5)}
.dots i.on{background:var(--white)}

/* features */
.photo-frame{background:var(--white);box-shadow:0 2px 10px rgba(0,0,0,.25);padding:17px}
.photo{width:100%;height:100%}
.ph-cookie{background:radial-gradient(ellipse at 70% 75%,#a78457 0%,#6e5338 45%,#3e4248 100%)}
.ph-cake{background:radial-gradient(ellipse at 45% 45%,#9a6a3e 0%,#6a4427 45%,#3a2f2b 100%)}
.feature-title{font-family:"Aleo",Georgia,serif;font-size:35px;font-weight:400;color:var(--ink)}
.feature-sub{font-family:"Aleo",Georgia,serif;font-size:18px;font-weight:700;color:var(--ink)}
.feature-text{font-size:12.5px;line-height:20px;color:var(--muted);width:445px}
.btn{display:flex;align-items:center;justify-content:space-between;padding:0 20px;border:2px solid var(--red);color:var(--red);font-size:13px;font-weight:600;letter-spacing:.5px;width:170px;height:42px;text-transform:uppercase}
.right{text-align:right}

/* tabs band */
.band{left:0;top:1507px;width:1200px;height:512px;background:radial-gradient(ellipse 700px 300px at 50% 20%,#f0363c 0%,transparent 70%),linear-gradient(180deg,#e8262d,#d81d24)}
.tab-panel{left:146px;top:1593px;width:908px;height:342px;background:var(--white)}
.tabs{display:flex;height:54px}
.tab{flex:1;display:flex;align-items:center;justify-content:center;font-family:"Aleo",Georgia,serif;font-size:18px;background:var(--tab);border-left:1px solid #cfcfcf;border-bottom:1px solid #cfcfcf;color:var(--ink)}
.tab.active{background:var(--white);color:var(--red);border:none}
.thumb{top:91px;width:240px;height:186px}
.ph-bowl{background:linear-gradient(160deg,#d7d7d7,#8d8d8d 55%,#4c4c4c)}
.ph-muffin{background:radial-gradient(ellipse at 50% 50%,#8b5e3b,#4a2f1e 70%,#2a1d16)}
.ph-dough{background:radial-gradient(ellipse at 55% 60%,#b8915e,#8d7457 50%,#6f7a82)}
.caption{top:300px;width:240px;text-align:center;color:var(--red);font-size:13px;font-weight:600}
.arrow{top:172px;width:16px;height:24px}

/* testimonials */
.info-box{left:146px;top:2077px;width:908px;height:204px;background:var(--white);box-shadow:0 1px 8px rgba(0,0,0,.22)}
.divider{left:561px;top:22px;width:1px;height:160px;background:var(--line)}
.box-title{font-family:"Aleo",Georgia,serif;font-weight:700;color:var(--red);font-size:18px;text-align:center}
.quote-name{font-family:"Aleo",Georgia,serif;font-weight:700;font-size:14px;text-align:center}
.quote{font-style:italic;font-size:12px;line-height:19px;color:var(--muted);text-align:center}
.about-text{font-size:12px;line-height:19px;color:var(--muted);text-align:center}
.avatar{border-radius:50%}

/* footer */
.footer{left:0;top:2345px;width:1200px;height:287px;background:var(--black);border-top:4px solid #3a3a3a}
.foot-head{font-size:15px;color:var(--white);letter-spacing:.5px;text-transform:uppercase}
.foot-list{list-style:none;font-size:11px;color:#d0d0d0}
.foot-list li{height:21px;display:flex;align-items:center;gap:8px}
.foot-list li::before{content:"";width:4px;height:4px;background:var(--red);border-radius:50%}
.foot-list.strong{font-weight:600;color:var(--white)}
.contact-line{font-size:11px;color:#d0d0d0;line-height:18px;display:flex;gap:10px}
.foot-brand{font-family:"Aleo",Georgia,serif;font-weight:700;font-size:26px;color:var(--white)}
.copyright{font-size:9.5px;color:#8a8a8a}
.social{display:flex;gap:7px}
.social i{width:20px;height:20px;display:block}
</style>
</head>
<body>

<header class="abs hero">
  <div class="hero-photo" role="img" aria-label="Galletas recién horneadas en primer plano"></div>
  <div class="hero-shade"></div>
  <div class="abs menu-icon"><span></span><span></span><span></span></div>
  <div class="abs brand-badge"><span>Panes<br>Doradillos</span></div>
  <h1 class="abs hero-title">We have been baking and crating all sorts of cookies<br>and cakes for <strong>more than 35 years</strong></h1>
  <div class="abs dots"><i class="on"></i><i></i></div>
</header>

<section>
  <div class="abs photo-frame" style="left:126px;top:642px;width:453px;height:370px">
    <div class="photo ph-cookie" role="img" aria-label="Masa de galletas con chispas de chocolate en bandeja"></div>
  </div>
  <h2 class="abs feature-title" style="left:647px;top:664px">Sorts of cookies</h2>
  <p class="abs feature-sub" style="left:647px;top:717px">You'll love our delicous fast food</p>
  <p class="abs feature-text" style="left:647px;top:761px">Lorem ipsum dolor sit amet, consectetur adipisic ing elit, sed do eiusmod tempor incididunt ut labore et dolore magna aliqua. Ut enim ad minim veniam, quis nostrud exercitation ullamco laboris nisi ut aliquip ex ea commodo consequat. Duis aute irure dolor in re prehenderit in voluptate velit esse cillum dolore eu fugiat nulla pariatur. Exce teur sint occaecat cup.</p>
  <a class="abs btn" style="left:647px;top:893px">Read more
    <svg width="18" height="12" viewBox="0 0 18 12"><path d="M0 6h16M11 1l5 5-5 5" fill="none" stroke="#ec2027" stroke-width="2"/></svg></a>

  <div class="abs photo-frame" style="left:624px;top:1054px;width:455px;height:370px">
    <div class="photo ph-cake" role="img" aria-label="Rebanada de pastel de zanahoria con almendras"></div>
  </div>
  <h2 class="abs feature-title right" style="right:611px;top:1076px">Crating Cakes</h2>
  <p class="abs feature-sub right" style="right:611px;top:1129px">You'll love our delicous fast food</p>
  <p class="abs feature-text right" style="right:611px;top:1180px">Lorem ipsum dolor sit amet, consectetur adipisic ing elit, sed do eiusmod tempor incididunt ut labore et dolore magna aliqua. Ut enim ad minim veniam, quis nostrud exercitation ullamco laboris nisi ut aliquip ex ea commodo consequat. Duis aute irure dolor in re prehenderit in voluptate velit esse cillum dolore eu fugiat nulla pariatur. Exce teur sint occaecupi datat.</p>
  <a class="abs btn" style="left:417px;top:1310px">Read more
    <svg width="18" height="12" viewBox="0 0 18 12"><path d="M0 6h16M11 1l5 5-5 5" fill="none" stroke="#ec2027" stroke-width="2"/></svg></a>
</section>

<section>
  <div class="abs band" role="img" aria-label="Fondo rojo con utensilios de repostería desenfocados"></div>
  <div class="abs tab-panel">
    <div class="tabs">
      <div class="tab active">Baking</div>
      <div class="tab">Cookies</div>
      <div class="tab">Cakes</div>
      <div class="tab">Crating</div>
    </div>
    <svg class="abs arrow" style="left:29px" viewBox="0 0 16 24"><path d="M12 3L4 12l8 9" fill="none" stroke="#ec2027" stroke-width="3"/></svg>
    <div class="abs thumb ph-bowl" style="left:61px" role="img" aria-label="Batidora de acero en la cocina"></div>
    <div class="abs thumb ph-muffin" style="left:335px" role="img" aria-label="Panecillo con pasas partido"></div>
    <div class="abs thumb ph-dough" style="left:608px" role="img" aria-label="Galletas crudas sobre bandeja"></div>
    <p class="abs caption" style="left:61px">Sed ut perspiciatis</p>
    <p class="abs caption" style="left:335px">Sed ut perspiciatis</p>
    <p class="abs caption" style="left:608px">Sed ut perspiciatis</p>
    <svg class="abs arrow" style="left:862px" viewBox="0 0 16 24"><path d="M4 3l8 9-8 9" fill="none" stroke="#ec2027" stroke-width="3"/></svg>
  </div>
</section>

<section class="abs info-box">
  <h3 class="abs box-title" style="left:0;top:20px;width:561px">Our Happy Customers</h3>
  <p class="abs quote-name" style="left:0;top:52px;width:561px">Marco Ledesma</p>
  <p class="abs quote" style="left:80px;top:76px;width:400px">Lorem ipsum dolor sit amet, consectetur adipisic ing elit, sed do eiusmod tempor incididunt ut labore et dolore magna aliqua.</p>
  <svg class="abs" style="left:170px;top:144px" width="220" height="50" viewBox="0 0 220 50">
    <path d="M12 17l-6 8 6 8" fill="none" stroke="#ec2027" stroke-width="2.5"/>
    <circle cx="47" cy="25" r="19" fill="#7a6a60"/>
    <circle cx="110" cy="25" r="24" fill="#c96b5c" stroke="#ec2027" stroke-width="2"/>
    <circle cx="172" cy="25" r="19" fill="#9a9a9a"/>
    <path d="M208 17l6 8-6 8" fill="none" stroke="#ec2027" stroke-width="2.5"/>
  </svg>
  <div class="abs divider"></div>
  <h3 class="abs box-title" style="left:562px;top:20px;width:346px">Abourt PD</h3>
  <p class="abs about-text" style="left:590px;top:52px;width:290px">Lorem ipsum dolor sit amet, consectetur adipisic ing elit, sed do eiusmod tempor incididunt ut labore et dolore magna aliqua. Ut enim ad minim veniam, quis nostrud exercitation ullamco laboris nisi ut aliquip ex ea commodo consequat. Duis aute irure dolor in re prehenderit in</p>
</section>

<footer class="abs footer">
  <h4 class="abs foot-head" style="left:98px;top:26px">Information</h4>
  <ul class="abs foot-list strong" style="left:98px;top:64px">
    <li>About Us</li><li>History</li><li>Career</li><li>Excutive Team</li>
  </ul>
  <h4 class="abs foot-head" style="left:368px;top:26px">Services</h4>
  <ul class="abs foot-list" style="left:368px;top:64px">
    <li>Sed ut perspiciatis unde</li><li>Wmnis iste natus error</li><li>Sit voluptatem accusan-</li><li>Tium doloremque Lau-</li><li>dantium, totam rem</li>
  </ul>
  <h4 class="abs foot-head" style="left:670px;top:26px">Products</h4>
  <ul class="abs foot-list" style="left:670px;top:64px">
    <li>Sed ut perspiciatis unde</li><li>Wmnis iste natus error</li><li>Sit voluptatem accusan-</li><li>Tium doloremque</li><li>Laudantium, totam rem</li>
  </ul>
  <h4 class="abs foot-head" style="left:938px;top:26px">Contacts</h4>
  <div class="abs contact-line" style="left:940px;top:64px">
    <svg width="10" height="14" viewBox="0 0 10 14"><path d="M5 0a5 5 0 0 1 5 5c0 4-5 9-5 9S0 9 0 5a5 5 0 0 1 5-5z" fill="#fff"/><circle cx="5" cy="5" r="2" fill="#121212"/></svg>
    <span>Calle Roble 214, Col. Juárez,<br>CDMX 06600</span>
  </div>
  <div class="abs contact-line" style="left:940px;top:112px">
    <svg width="10" height="14" viewBox="0 0 10 14"><rect x="1" y="0" width="8" height="14" rx="1.5" fill="#fff"/><rect x="2.5" y="2" width="5" height="8" fill="#121212"/></svg>
    <span>+52 55 4821 7730<br>+52 55 4821 7731</span>
  </div>
  <div class="abs contact-line" style="left:940px;top:154px">
    <svg width="12" height="14" viewBox="0 0 12 14"><rect x="0" y="3" width="12" height="8" fill="#fff"/><path d="M0 3l6 5 6-5" fill="none" stroke="#121212" stroke-width="1"/></svg>
    <span>hola@panesdoradillos.mx</span>
  </div>
  <p class="abs foot-brand" style="left:98px;top:212px">Tomelo</p>
  <p class="abs copyright" style="left:726px;top:235px">© 2014 Panes Doradillos all rights are reserved</p>
  <div class="abs social" style="left:970px;top:231px">
    <i style="background:#2f63b0"></i><i style="background:#2aa3df"></i><i style="background:#2f63b0"></i><i style="background:#1fb6e0"></i><i style="background:#d9473b"></i>
  </div>
</footer>

</body>
</html>
```